SPICE LABEL DESIGN FOR A TASTY DRY RUB! (chicken, ribs, wings)

Looking for a fun/creative/edgy label for a spice jar! The label will be rectangular (exact size tbd - but approximately 1.2" W X 3" H).
This spice is a dry rub blend of 14 EPIC spices, to be used on chicken, chicken wings, ribs, etc.
Copywritting on the label to be;
Nel DX's Blaze BBQ Rub
A blend of 14 UNNELEIVABLE spices
*Note the word "unneleivabe" is spelt incorectly on purpose for a play a words with "nel". Please use a different color font for "nel" within the word.
Also would like "Nel DX's" to be prominent
Looking for an illustration/design that is fun/creative/catchy/edgy/appealing! While still keeping the design appealing to higher end markets. Have fun with it and think outside of the box!! :)
People who enjoy cooking, young adults and adults, display at restaurants or retail markets

```html
<!DOCTYPE html>
<html lang="en">
<head>
<meta charset="utf-8">
<title>Nel DX's Blaze BBQ Rub – Spice Label</title>
<link rel="stylesheet" href="https://fonts.googleapis.com/css2?family=Alfa+Slab+One&family=Oswald:wght@600;700&family=Montserrat:wght@600;700&display=swap">
<style>
  :root {
    --backdrop: #fbd0a9;
    --label-white: #ffffff;
    --teal: #41bcb9;
    --maroon: #8b1a2b;
    --slate: #6d6e71;
    --blush: #efc9c6;
    --feather: #f4f1ec;
  }
  * { margin: 0; padding: 0; box-sizing: border-box; }
  html, body {
    width: 961px; height: 1200px; overflow: hidden;
    background: var(--backdrop);
  }
  .label {
    position: absolute; left: 329px; top: 222px;
    width: 302px; height: 756px;
    background: var(--label-white);
    overflow: hidden;
  }
  .brand-band {
    position: absolute; left: 0; top: 0; width: 100%; height: 84px;
    background: var(--teal);
    display: flex; align-items: center; justify-content: center;
  }
  .brand-name {
    font-family: "Alfa Slab One", serif; font-weight: 400;
    font-size: 44px; color: var(--label-white); letter-spacing: 1px;
  }
  .brand-rule {
    position: absolute; left: 0; top: 91px; width: 100%; height: 3px;
    background: var(--teal);
  }
  .flavour {
    position: absolute; left: 0; top: 128px; width: 100%;
    display: flex; align-items: center; justify-content: center; gap: 12px;
  }
  .flavour-dash { width: 32px; height: 3px; background: var(--slate); }
  .flavour-word {
    font-family: "Alfa Slab One", serif;
    font-size: 32px; color: var(--slate); letter-spacing: 1px; line-height: 40px;
  }
  .product {
    position: absolute; left: 0; width: 100%; text-align: center;
    font-family: "Alfa Slab One", serif;
    font-size: 86px; line-height: 1; color: var(--maroon);
    letter-spacing: 8px; text-indent: 8px;
  }
  .product-bbq { top: 170px; }
  .product-rub { top: 252px; }
  .garnish {
    position: absolute; background: var(--blush); opacity: 0.7;
  }
  .garnish-slice-top { left: -14px; top: 344px; width: 56px; height: 66px; border-radius: 50%; }
  .garnish-pepper-top { left: 250px; top: 322px; width: 52px; height: 122px; border-radius: 40px 10px 40px 40px; }
  .garnish-pepper-low { left: 0; top: 612px; width: 28px; height: 112px; border-radius: 10px 30px 30px 10px; }
  .garnish-slice-low { left: 262px; top: 646px; width: 60px; height: 80px; border-radius: 50%; }
  .mascot {
    position: absolute; left: 53px; top: 342px;
    width: 192px; height: 228px;
  }
  .mascot-disc {
    position: absolute; left: 10px; top: 40px;
    width: 176px; height: 176px; border-radius: 50%;
    background: var(--teal);
  }
  .mascot-figure {
    position: absolute; left: 46px; top: 4px;
    width: 104px; height: 212px; border-radius: 52px;
    background: linear-gradient(180deg, var(--feather), #e9e4dc);
  }
  .blend-bar {
    position: absolute; left: 30px; top: 581px; width: 234px; height: 23px;
    background: var(--teal);
    display: flex; align-items: center; justify-content: center;
    font-family: "Montserrat", sans-serif; font-weight: 700;
    font-size: 15px; color: var(--label-white); letter-spacing: 3px;
  }
  .spice-count {
    position: absolute; left: 0; top: 608px; width: 100%; text-align: center;
    font-family: "Alfa Slab One", serif;
    font-size: 48px; line-height: 52px; color: var(--maroon);
  }
  .tagline {
    position: absolute; left: 0; top: 656px; width: 100%; text-align: center;
    font-family: "Oswald", sans-serif; font-weight: 700;
    font-size: 38px; line-height: 44px; color: var(--slate);
    letter-spacing: 1.5px;
  }
  .tagline-name { color: var(--maroon); }
  .spices-word {
    position: absolute; left: 0; top: 701px; width: 100%; text-align: center;
    font-family: "Montserrat", sans-serif; font-weight: 600;
    font-size: 16px; color: var(--slate); letter-spacing: 4px; text-indent: 4px;
  }
  .foot-band {
    position: absolute; left: 0; bottom: 0; width: 100%; height: 26px;
    background: var(--teal);
  }
</style>
</head>
<body>
  <main class="label">
    <header class="brand-band"><h1 class="brand-name">NEL DX'S</h1></header>
    <div class="brand-rule"></div>

    <div class="flavour">
      <span class="flavour-dash"></span>
      <span class="flavour-word">BLAZE</span>
      <span class="flavour-dash"></span>
    </div>
    <div class="product product-bbq">BBQ</div>
    <div class="product product-rub">RUB</div>

    <div class="garnish garnish-slice-top" role="img" aria-label="Faint sketched tomato slice decoration"></div>
    <div class="garnish garnish-pepper-top" role="img" aria-label="Faint sketched chili pepper decoration"></div>
    <div class="garnish garnish-pepper-low" role="img" aria-label="Faint sketched chili pepper decoration"></div>
    <div class="garnish garnish-slice-low" role="img" aria-label="Faint sketched tomato slice decoration"></div>

    <div class="mascot" role="img" aria-label="Cartoon white rooster giving an OK gesture in front of a teal circle">
      <div class="mascot-disc"></div>
      <div class="mascot-figure"></div>
    </div>

    <div class="blend-bar">A BLEND OF</div>
    <div class="spice-count">14</div>
    <div class="tagline">UN<span class="tagline-name">NEL</span>EIVABLE</div>
    <div class="spices-word">SPICES</div>
    <footer class="foot-band"></footer>
  </main>
</body>
</html>
```